Eneginering consultancy brochure style web design project

Looking for a new brochure style web page for our small engineering consultancy. The prupose of the website is to provide some basic information with about the company, including exampels of our work, and present a way to initiate contact. There there will only be a few pages (up to 5) and limited content.A main focus of the project is to develop the visual design/identity for the webpage, and to provide the template for us to add content, rearrange layout and modify pages with relative ease.A mixture of text and images will be used. The use of an image slider would be desirable.We have recently had a new company logo developed (uploaded), which defines the colour scheme for the page.A professional. clean look is desired, that is not cluttered and easy to navigate.Template to add a photo slider is desirable.The use of swirl patterns (suach as those used here: https://www.brightvortex.co.uk/) and/or contoured mesh pattern (example attached) within the page is likely to be attractive, as this is in harmony with our activities.

Target Market(s)

Engineering; manufacturing

Industry/Entity Type

Engineering Consultant

Coding

Coded - Design and coding required

Number of Pages Required

3 page

Font styles to use
Other font styles liked:
• Helvetica

Colors
00a990
33b8a4
86cfc6
606060
3176b5
0255a3
85acd3
474747
7f7f7f

Requirements
Must have
• 1) Landing page for information about the company. Mostly text, with image slider.
• 2) One page for example projects. Images with accompanying texts.
• 3) Enquiry/'get in touch' page.
• Simple, uncluttered look and feel.

```html
<!DOCTYPE html>
<html lang="en">
<head>
<meta charset="utf-8">
<title>TCE – Thermal Core Engineering</title>
<link href="https://fonts.googleapis.com/css2?family=Arimo:wght@400;700&display=swap" rel="stylesheet">
<style>
:root{
  --teal:#00a990;
  --teal-mid:#33b8a4;
  --teal-soft:#86cfc6;
  --blue:#0255a3;
  --blue-mid:#3176b5;
  --blue-soft:#85acd3;
  --grey:#606060;
  --grey-dark:#474747;
  --grey-light:#7f7f7f;
  --panel:#eef3fa;
  --tile:#e9e9ea;
  --footer:#2c2c2c;
  --white:#ffffff;
}
*{box-sizing:border-box;margin:0;padding:0}
html,body{width:1200px;height:3579px;overflow:hidden}
body{position:relative;background:var(--white);font-family:"Arimo",Helvetica,Arial,sans-serif;color:var(--grey)}
.abs{position:absolute}
.photo{position:absolute;overflow:hidden}

/* header */
.site-header{left:0;top:0;width:1200px;height:120px;background:var(--white)}
.brand{left:143px;top:40px;display:flex;align-items:center;gap:12px}
.brand-mark{width:30px;height:30px;background:var(--teal);border-radius:50%}
.brand-name{font-size:21px;font-weight:700;color:var(--blue);line-height:1}
.enquire{left:935px;top:26px;width:120px;height:34px;background:var(--teal);color:var(--white);font-size:13px;display:flex;align-items:center;justify-content:center;border-radius:2px}
.main-nav{top:82px;font-size:14px;color:var(--grey-dark)}
.main-nav.active{color:var(--blue)}

/* hero */
.hero{left:0;top:120px;width:1200px;height:545px}
.hero-title{left:0;top:286px;width:1200px;text-align:center;color:var(--white);font-size:31px;line-height:39px;font-weight:400}
.hero-btn{left:540px;top:372px;width:120px;height:36px;background:var(--white);color:var(--blue);font-size:12px;display:flex;align-items:center;justify-content:center;border-radius:2px}
.hero-arrow{top:350px;width:36px;height:36px}

/* about */
.about-box{left:143px;top:742px;width:456px;height:399px;background:var(--teal);color:var(--white);padding:25px 22px}
.about-box h2{font-size:31px;font-weight:400;margin-bottom:12px}
.about-box p{font-size:11.5px;line-height:17px;margin-bottom:15px}
.director-name{left:790px;top:1046px;font-size:32px;color:var(--blue)}
.director-role{left:790px;top:1094px;font-size:14px;color:var(--grey-light)}
.director-link{left:790px;top:1122px;width:20px;height:20px;background:var(--grey)}

/* services */
.services-panel{left:599px;top:1293px;width:601px;height:465px;background:var(--panel);padding:36px 50px 0 48px}
.services-panel h2{font-size:31px;font-weight:400;color:var(--blue);margin-bottom:20px}
.services-panel p{font-size:11.5px;line-height:17px;margin-bottom:16px}
.services-panel ul{list-style:none;margin-bottom:16px}
.services-panel li{font-size:11.5px;line-height:25px}
.services-panel li::before{content:"•";margin-right:10px}

/* software */
.tool-cell{position:absolute;background:var(--tile);display:flex;align-items:center;justify-content:center;flex-direction:column;gap:12px}
.tool-shape{width:40px;height:40px;background:var(--grey-light);border-radius:50%}
.tool-shape.square{border-radius:0}
.tool-name{font-size:18px;color:var(--grey-dark)}
.software-box{left:599px;top:1899px;width:456px;height:368px;background:var(--blue);color:var(--white);padding:30px 22px}
.software-box h2{font-size:31px;font-weight:400;margin-bottom:10px}
.software-box p{font-size:11.5px;line-height:17px;margin-bottom:17px}

/* work */
.work-band{left:0;top:2346px;width:1200px;height:632px;background:var(--panel)}
.section-title{left:0;width:1200px;text-align:center;font-size:31px;color:var(--blue);font-weight:400}
.work-card{position:absolute;width:297px}
.work-arrow{position:absolute;right:0;bottom:0;width:46px;height:46px;background:var(--blue);display:flex;align-items:center;justify-content:center}

/* contact */
.field{position:absolute;border:1px solid #cfcfcf;background:var(--white);font-size:11px;color:var(--grey-light);padding:0 14px;display:flex;align-items:center}
.field.message{align-items:flex-start;padding-top:14px}
.submit{left:561px;top:3312px;width:79px;height:34px;background:var(--blue);color:var(--white);font-size:11px;font-weight:700;display:flex;align-items:center;justify-content:center;border-radius:3px}
.footer-fade{left:0;top:3380px;width:1200px;height:84px;background:linear-gradient(180deg,#ffffff,#e9eef4)}

/* footer */
.site-footer{left:0;top:3464px;width:1200px;height:115px;background:var(--footer)}
.footer-links{left:143px;top:3497px;font-size:11px;color:var(--blue-soft)}
.footer-copy{left:143px;top:3532px;font-size:11px;color:var(--grey-light)}
.follow{left:871px;top:3431px;width:329px;height:148px;background:var(--blue);color:var(--white);padding:28px 34px}
.follow p{font-size:12px;margin-bottom:34px}
.social{display:flex;gap:30px}
.social span{width:26px;height:26px;border-radius:50%;background:var(--white)}
</style>
</head>
<body>

<header class="abs site-header">
  <div class="abs brand"><span class="brand-mark"></span><span class="brand-name">Thermal Core Engineering</span></div>
  <div class="abs enquire">ENQUIRE NOW</div>
  <span class="abs main-nav active" style="left:616px">Home</span>
  <span class="abs main-nav" style="left:692px">About Us</span>
  <span class="abs main-nav" style="left:792px">Services</span>
  <span class="abs main-nav" style="left:885px">Software</span>
  <span class="abs main-nav" style="left:983px">Contact Us</span>
</header>

<svg class="abs hero" viewBox="0 0 1200 545" preserveAspectRatio="none" role="img" aria-label="Engineers reviewing electrical machine designs on a screen">
  <defs>
    <linearGradient id="heroTone" x1="0" y1="0" x2="1" y2="1">
      <stop offset="0" stop-color="#4f5c66"/>
      <stop offset=".45" stop-color="#8b98a2"/>
      <stop offset=".75" stop-color="#aab4bb"/>
      <stop offset="1" stop-color="#6e7b85"/>
    </linearGradient>
  </defs>
  <path d="M0 0 H1200 V440 C1080 420 950 470 760 500 C500 540 250 510 0 450 Z" fill="url(#heroTone)"/>
</svg>
<h1 class="abs hero-title">Thermal Design, Simulations and Analysis of<br>electrical machines</h1>
<div class="abs hero-btn">GET IN TOUCH</div>
<svg class="abs hero-arrow" style="left:46px" viewBox="0 0 36 36"><path d="M22 8 L12 18 L22 28" fill="none" stroke="#fff" stroke-width="4"/></svg>
<svg class="abs hero-arrow" style="left:1116px" viewBox="0 0 36 36"><path d="M14 8 L24 18 L14 28" fill="none" stroke="#fff" stroke-width="4"/></svg>

<section class="abs about-box">
  <h2>About Company</h2>
  <p>TCE is a thermal engineering consultancy, specialising in the thermal design, simulation and analysis of electrical machines.</p>
  <p>Our experience spans across traditional and novel machine arrangements, with extensive experience with Permanent Magnet, Induction, Synchronous, Switched Reluctance and Synchronous Reluctance machines.</p>
  <p>Machines have been designed to operate in a range of applications and environments including automotive, aerospace, marine, energy generation and energy recovery.</p>
  <p>Using a comprehensive skillset, we can provide a complete thermal analysis for your engineering project. Our close links with different collaborators also allows for us to perform multi-domain analysis, covering the electro-magnetic and mechanical aspects of designs.</p>
</section>
<div class="photo" style="left:599px;top:742px;width:456px;height:289px;background:linear-gradient(135deg,#eef0f1,#d5d9dc 55%,#b9aa9c)" role="img" aria-label="Hand sketching a technical drawing on a desk"></div>
<div class="photo" style="left:599px;top:1031px;width:176px;height:181px;background:linear-gradient(160deg,#9a988c,#5e5a52)" role="img" aria-label="Portrait of the managing director"></div>
<div class="abs director-name">Daniel Marsh</div>
<div class="abs director-role">Managing Director</div>
<div class="abs director-link"></div>

<div class="photo" style="left:0;top:1341px;width:599px;height:477px;background:linear-gradient(135deg,#7a7e83,#a8453a 45%,#c25044 65%,#506f9c)" role="img" aria-label="Technician working on a large red electric motor"></div>
<section class="abs services-panel">
  <h2>Our Services</h2>
  <p>TCE offers thermal analysis and design for electrical machine design projects. We use a range of both commercial and in-house software for the design and optimisation of electrical machines using a multi-physics approach.</p>
  <p>TCE can assist through all stages of your project:</p>
  <ul>
    <li>Experience and intuition for concept generation</li>
    <li>Thermo-fluid modelling and simulation for design development</li>
    <li>Application of a range of thermal simulation tools</li>
    <li>Test data acquisition for design validation and optimisation</li>
  </ul>
  <p>We also provide thermal analysis on existing designs, making recommendations to improve their thermal performance.</p>
</section>

<div class="tool-cell" style="left:143px;top:1899px;width:245px;height:158px"><span class="tool-shape"></span><span class="tool-name">Calcula</span></div>
<div class="tool-cell" style="left:393px;top:1899px;width:206px;height:158px"><span class="tool-shape square"></span><span class="tool-name">Flowsys</span></div>
<div class="tool-cell" style="left:143px;top:2062px;width:245px;height:158px"><span class="tool-shape square"></span><span class="tool-name">OpenFlux</span></div>
<div class="tool-cell" style="left:393px;top:2062px;width:206px;height:158px"><span class="tool-shape"></span><span class="tool-name">MotorSim</span></div>
<section class="abs software-box">
  <h2>Software</h2>
  <p>We are experienced with many different software packages, enabling us to select the most appropriate tools for each project. This includes CFD, thermal resistance modelling, analytical sizing tools and multi-objective optimisation tools.</p>
  <p>We also develop bespoke thermal analysis tools for novel machine types and applications which are beyond the limitations of commercial packages. These parameterised analysis tools can be used by us to design and optimise your design. Designed with user-friendliness in mind, they can also be designed for use by you and your design teams.</p>
  <p>We offer a professional approach to all work, using our experience to provide industry standard deliverables on the timescales agreed.</p>
</section>

<div class="abs work-band"></div>
<h2 class="abs section-title" style="top:2428px">Our Work</h2>
<div class="work-card" style="left:143px;top:2484px;height:198px;background:linear-gradient(135deg,#dcd6cf,#a88a76)" role="img" aria-label="Engineer assembling electronics on a workbench"><span class="work-arrow"><svg width="20" height="20" viewBox="0 0 20 20"><path d="M2 10H16M10 4L16 10L10 16" fill="none" stroke="#fff" stroke-width="3"/></svg></span></div>
<div class="work-card" style="left:451px;top:2484px;height:198px;background:linear-gradient(135deg,#3f4144,#a9acb0 55%,#6a6c70)" role="img" aria-label="Industrial electric motor"><span class="work-arrow"><svg width="20" height="20" viewBox="0 0 20 20"><path d="M2 10H16M10 4L16 10L10 16" fill="none" stroke="#fff" stroke-width="3"/></svg></span></div>
<div class="work-card" style="left:758px;top:2484px;height:198px;background:linear-gradient(135deg,#8a8f96,#b5642e 55%,#6b4a36)" role="img" aria-label="Copper motor windings being assembled"><span class="work-arrow"><svg width="20" height="20" viewBox="0 0 20 20"><path d="M2 10H16M10 4L16 10L10 16" fill="none" stroke="#fff" stroke-width="3"/></svg></span></div>
<div class="work-card" style="left:143px;top:2691px;height:201px;background:linear-gradient(135deg,#8c3a12,#c96a2a 50%,#6a2a0c)" role="img" aria-label="Close-up of copper coil winding"><span class="work-arrow"><svg width="20" height="20" viewBox="0 0 20 20"><path d="M2 10H16M10 4L16 10L10 16" fill="none" stroke="#fff" stroke-width="3"/></svg></span></div>
<div class="work-card" style="left:451px;top:2691px;height:201px;background:linear-gradient(135deg,#a2a29e,#b8a85a 50%,#555555)" role="img" aria-label="Measuring current in an electrical cabinet"><span class="work-arrow"><svg width="20" height="20" viewBox="0 0 20 20"><path d="M2 10H16M10 4L16 10L10 16" fill="none" stroke="#fff" stroke-width="3"/></svg></span></div>
<div class="work-card" style="left:758px;top:2691px;height:201px;background:linear-gradient(90deg,#cf9f4a,#8197c0 40%,#c8c8c8 65%,#c9824a)" role="img" aria-label="Bundles of coloured electrical cables"><span class="work-arrow"><svg width="20" height="20" viewBox="0 0 20 20"><path d="M2 10H16M10 4L16 10L10 16" fill="none" stroke="#fff" stroke-width="3"/></svg></span></div>

<h2 class="abs section-title" style="top:3052px">Contact</h2>
<div class="field" style="left:143px;top:3107px;width:219px;height:43px">Name</div>
<div class="field" style="left:375px;top:3107px;width:219px;height:43px">Email</div>
<div class="field" style="left:606px;top:3107px;width:219px;height:43px">Phone</div>
<div class="field" style="left:837px;top:3107px;width:218px;height:43px">Title</div>
<div class="field message" style="left:143px;top:3169px;width:912px;height:124px">Message</div>
<div class="abs submit">SUBMIT</div>

<div class="abs footer-fade"></div>
<footer class="abs site-footer"></footer>
<div class="abs footer-links">Home &nbsp;&nbsp;|&nbsp;&nbsp; About Us &nbsp;&nbsp;|&nbsp;&nbsp; Services &nbsp;&nbsp;|&nbsp;&nbsp; Software &nbsp;&nbsp;|&nbsp;&nbsp; Contact Us</div>
<div class="abs footer-copy">Copyright © 2019 &nbsp;Thermal Core Engineering. &nbsp;All rights reserved.</div>
<div class="abs follow">
  <p>Follow us on</p>
  <div class="social"><span></span><span></span><span></span></div>
</div>

</body>
</html>
```